Brisk Lark Delivery Service Wordpress design

My client is a delivery service whose motto is "We go where the freight leads us." Their colors are red, white and blue. They use Voyara vans and box vans - NO semi tractors. They like this Website design www.kwuzo.com, but I would like to see some designs that make them stand out. Attached is their new logo.

Target Market(s)

Businesses who use delivery services in town and anyone needing freight picked up or transported in the United States.

Industry/Entity Type

Delivery Service

Number of Pages Required

1 page

Font styles to use
Sans Serif

Colors
ec1f27
0455a3
ffffff

Requirements
Must have
• We need a Wordpress design with sliders that incorporates their new logo and the motto "WE GO WHERE THE FREIGHT LEADS US" Their corporate colors are red, white and blue. They only use voyara vans and box vans.
Nice to have
• Please use your creativity to come up with a unique design for this delivery service.
Should not have
• NO SEMI TRACTOR TRAILERS

```html
<!DOCTYPE html>
<html lang="en">
<head>
<meta charset="utf-8">
<title>Brisk Lark Delivery Service</title>
<link rel="stylesheet" href="https://fonts.googleapis.com/css2?family=Montserrat:wght@500;600;700;800&family=Lato:wght@400;700&display=swap">
<style>
:root{
  --navy:#1d1a5c;
  --navy-deep:#16124f;
  --red:#ec1f27;
  --blue:#0455a3;
  --white:#ffffff;
  --ink:#444452;
  --grey-band:#e4e4e4;
  --card:#efefef;
  --line:#d6d6d6;
}
*{margin:0;padding:0;box-sizing:border-box}
html,body{width:1200px;height:2442px;overflow:hidden}
body{position:relative;background:var(--white);font-family:"Lato",sans-serif;color:var(--ink)}
.abs{position:absolute}
h1,h2,h3,.nav a,.btn{font-family:"Montserrat",sans-serif}

/* header */
.topbar{left:0;top:0;width:1200px;height:68px;background:#f5f5f5}
.brand{left:208px;top:14px;display:flex;align-items:center;gap:12px}
.brand-name{font-family:"Montserrat",sans-serif;font-weight:800;font-size:24px;color:var(--navy);letter-spacing:.5px}
.brand-dot{width:38px;height:38px;border-radius:50%;background:var(--red)}
.info{top:18px;display:flex;align-items:center;gap:12px;font-size:11px;line-height:14px;color:#222}
.info b{font-weight:700}
.info svg{width:22px;height:22px}
.hours{left:676px}
.call{left:879px}

.nav{left:0;top:68px;width:1200px;height:36px;background:var(--navy)}
.nav ul{list-style:none;position:absolute;left:208px;top:0;display:flex;height:36px}
.nav li{display:flex;align-items:center;border-right:1px solid rgba(255,255,255,.25);padding:0 16px}
.nav li:first-child{padding-left:0}
.nav li:last-child{border:none}
.nav a{color:var(--white);text-decoration:none;font-weight:700;font-size:13px}
.quote-tab{left:765px;top:68px;width:435px;height:36px}
.quote-tab span{position:absolute;left:20px;width:226px;top:0;line-height:36px;text-align:center;color:#fff;font-family:"Montserrat",sans-serif;font-weight:700;font-size:13px}

/* hero */
.hero{left:0;top:104px;width:1200px;height:295px;background:linear-gradient(100deg,#6b6d70 0%,#8a8c86 35%,#a08a4c 70%,#6f6a3c 100%)}
.hero-title{left:208px;top:148px;font-weight:800;font-size:42px;line-height:44px;letter-spacing:-1.5px;color:var(--white)}
.hero-title em{font-style:normal;color:var(--red)}
.btn{display:flex;align-items:center;justify-content:center;gap:12px;color:#fff;font-weight:600;text-decoration:none}
.hero-btn{left:208px;top:304px;width:180px;height:36px;background:var(--navy);font-size:12px;clip-path:polygon(0 0,100% 0,94% 100%,0 100%)}

/* who we are */
.who-photo{left:210px;top:470px;width:246px;height:370px;background:linear-gradient(160deg,#c9c6bd,#9e8f7a 60%,#6e6a66)}
.who-frame{left:220px;top:480px;width:246px;height:370px;border:2px solid var(--red)}
.section-title{font-weight:700;font-size:22px;color:var(--navy);text-transform:uppercase}
.section-title::after{content:"";display:block;width:40px;height:3px;background:var(--red);margin-top:8px}
.who-title{left:544px;top:467px}
.who-text{left:544px;top:521px;width:442px;font-size:11px;line-height:16px;color:#555}
.who-list{left:544px;top:684px;width:270px;list-style:none;font-size:11px;color:var(--navy);white-space:nowrap}
.who-list li{display:flex;align-items:center;gap:8px;height:21px}
.who-list svg{width:11px;height:11px;flex:none}
.small-btn{height:26px;background:var(--red);font-size:10px;clip-path:polygon(0 0,100% 0,92% 100%,0 100%)}
.who-btn{left:544px;top:807px;width:142px}
.trucks{left:770px;top:676px;width:320px;height:180px;background:radial-gradient(ellipse at center,#f2f2f2 0%,#dcdcdc 55%,#ffffff 72%)}

/* featured */
.featured{left:0;top:882px;width:1200px;height:453px;background:var(--grey-band)}
.feat-title{left:210px;top:915px}
.feat-text{left:210px;top:966px;width:580px;font-size:11px;line-height:16px;color:#555}
.card{width:381px;height:112px;background:var(--card);border:1px solid var(--line)}
.card-img{position:absolute;left:0;top:0;width:114px;height:110px;clip-path:polygon(0 0,100% 0,82% 100%,0 100%)}
.card h3{position:absolute;left:133px;top:18px;font-size:13px;font-weight:700;color:var(--navy)}
.card p{position:absolute;left:133px;top:42px;width:200px;font-size:10.5px;line-height:16px;color:#555}
.img-a{background:linear-gradient(135deg,#b7b3a8,#7a6f60)}
.img-b{background:linear-gradient(135deg,#8a7a5c,#d9d6cf 60%,#5a5f66)}
.img-c{background:linear-gradient(135deg,#a98a5e,#6a6f58)}

/* news */
.news-title{left:210px;top:1368px}
.view-all{left:944px;top:1380px;font-family:"Montserrat",sans-serif;font-weight:700;font-size:10px;color:var(--red)}
.news-img{width:181px;height:181px}
.news-date{font-family:"Montserrat",sans-serif;font-weight:700;font-size:34px;color:#222}
.news-date small{font-size:20px;font-weight:600}
.news-head{font-family:"Montserrat",sans-serif;font-weight:700;font-size:12px;color:#222}
.news-text{width:182px;font-size:10.5px;line-height:16px;color:#555}
.news-btn{width:140px}

/* clients */
.clients-title{left:210px;top:1711px}
.client{top:1776px;height:64px;width:160px;display:flex;align-items:center;justify-content:center;gap:8px;font-family:"Montserrat",sans-serif;font-weight:700;font-size:26px;color:#8a8a8a;white-space:nowrap}
.client i{display:block;width:16px;height:16px;background:#8a8a8a;border-radius:50%}

/* map + contact */
.map{left:0;top:1880px;width:1200px;height:321px;background:linear-gradient(135deg,#dfe6d3,#eae6d8 40%,#d9e3c9 70%,#b9d3e6 100%)}
.contact-box{left:319px;top:1880px;width:231px;height:191px;background:var(--navy)}
.contact-box h2{position:absolute;left:0;width:100%;top:18px;text-align:center;font-weight:700;font-size:16px;color:#fff}
.contact-box ul{position:absolute;left:30px;top:62px;list-style:none;color:#fff;font-size:13px}
.contact-box li{display:flex;align-items:center;gap:10px;height:21px}
.contact-box svg{width:13px;height:13px}
.map-pin{left:864px;top:1944px;width:40px;height:58px}

/* footer */
.footer{left:0;top:2201px;width:1200px;height:241px;background:var(--navy-deep)}
.fcol{top:2245px;color:#d7d6ea;font-size:9.5px;line-height:15px}
.fcol h4{font-family:"Montserrat",sans-serif;font-weight:700;font-size:9.5px;color:#fff;margin-bottom:6px}
.fcol ul{list-style:none}
.fcol li::before{content:"› "}
.loc{display:grid;grid-template-columns:70px 66px 60px;column-gap:6px;white-space:nowrap}
.copyright{left:0;top:2418px;width:1200px;text-align:center;font-size:8px;color:#8e8cb0}
</style>
</head>
<body>

<header>
  <div class="abs topbar"></div>
  <div class="abs brand"><span class="brand-name">BRISK LARK</span><span class="brand-dot"></span></div>
  <div class="abs info hours">
    <svg viewBox="0 0 24 24"><circle cx="12" cy="13" r="9" fill="none" stroke="#ec1f27" stroke-width="2.5"/><path d="M12 8v5l3 2" stroke="#ec1f27" stroke-width="2.2" fill="none"/></svg>
    <div><b>Mon - Fri 8.00 - 17.30</b><br>Weekend Closed</div>
  </div>
  <div class="abs info call">
    <svg viewBox="0 0 24 24"><path d="M6 2l4 4-2 3c1.5 3 4 5.5 7 7l3-2 4 4-3 4C10 21 3 14 2 5z" fill="#ec1f27"/></svg>
    <div><b>Call Us:</b><br>(555) 018 2264</div>
  </div>
  <nav class="abs nav">
    <ul>
      <li><a href="#">HOME</a></li>
      <li><a href="#">ABOUT US</a></li>
      <li><a href="#">SERVICE</a></li>
      <li><a href="#">NEWS</a></li>
      <li><a href="#">CONTACT US</a></li>
    </ul>
  </nav>
  <div class="abs quote-tab">
    <svg width="435" height="36" viewBox="0 0 435 36" style="position:absolute;left:0;top:0"><polygon points="0,0 435,0 435,36 22,36" fill="#ec1f27"/><rect x="20" y="3" width="226" height="30" fill="none" stroke="#fff" stroke-width="1"/></svg>
    <span>GET FREE QUOTE</span>
  </div>
</header>

<section>
  <div class="abs hero" role="img" aria-label="Smiling courier holding a parcel in front of a blurred delivery van on a country road"></div>
  <h1 class="abs hero-title"><em>WE</em> GO WHERE<br>THE <em>FREIGHT</em><br><em>LEADS</em> US</h1>
  <a class="abs btn hero-btn" href="#">GET FREE QUOTE
    <svg width="12" height="12" viewBox="0 0 12 12"><path d="M2 6h8M6 2l4 4-4 4" stroke="#fff" stroke-width="2" fill="none"/></svg></a>
</section>

<section>
  <div class="abs who-photo" role="img" aria-label="Courier unloading boxes from the back of a van"></div>
  <div class="abs who-frame"></div>
  <h2 class="abs section-title who-title">Who we are</h2>
  <p class="abs who-text">There are many variations of passages of Lorem Ipsum available, but the majority have suffered alteration in some form, by injected humour, or randomised words which don't look even slightly believable. If you are going to use a passage of Lorem Ipsum, you need to be sure there isn't anything embarrassing hidden in the middle of text. All the Lorem Ipsum generators on the Internet tend to repeat predefined chunks as necessary, making this the first true generator on the Internet. It uses a dictionary of over 200 Latin words, combined with a handful of model sentence structures, to generate Lorem Ipsum which looks reasonable. The generated Lorem Ipsum is therefore always free from repetition, injected humour, or non-characteristic words etc.</p>
  <ul class="abs who-list">
    <li><svg viewBox="0 0 12 12"><circle cx="6" cy="6" r="5" fill="none" stroke="#1d1a5c" stroke-width="1.3"/><path d="M5 3.5L7.5 6 5 8.5" stroke="#1d1a5c" stroke-width="1.3" fill="none"/></svg>Deliver Environmentally Responsible Client Services</li>
    <li><svg viewBox="0 0 12 12"><circle cx="6" cy="6" r="5" fill="none" stroke="#1d1a5c" stroke-width="1.3"/><path d="M5 3.5L7.5 6 5 8.5" stroke="#1d1a5c" stroke-width="1.3" fill="none"/></svg>Attractive Working Environment</li>
    <li><svg viewBox="0 0 12 12"><circle cx="6" cy="6" r="5" fill="none" stroke="#1d1a5c" stroke-width="1.3"/><path d="M5 3.5L7.5 6 5 8.5" stroke="#1d1a5c" stroke-width="1.3" fill="none"/></svg>Be an Active Community Partner</li>
    <li><svg viewBox="0 0 12 12"><circle cx="6" cy="6" r="5" fill="none" stroke="#1d1a5c" stroke-width="1.3"/><path d="M5 3.5L7.5 6 5 8.5" stroke="#1d1a5c" stroke-width="1.3" fill="none"/></svg>Maintain High Ethical Standards</li>
    <li><svg viewBox="0 0 12 12"><circle cx="6" cy="6" r="5" fill="none" stroke="#1d1a5c" stroke-width="1.3"/><path d="M5 3.5L7.5 6 5 8.5" stroke="#1d1a5c" stroke-width="1.3" fill="none"/></svg>Drive Continuous Improvement</li>
  </ul>
  <a class="abs btn small-btn who-btn" href="#">VIEW OUR SERVICES
    <svg width="10" height="10" viewBox="0 0 12 12"><path d="M2 6h8M6 2l4 4-4 4" stroke="#fff" stroke-width="2" fill="none"/></svg></a>
  <div class="abs trucks" role="img" aria-label="White cargo van and white box van side by side"></div>
</section>

<section>
  <div class="abs featured"></div>
  <h2 class="abs section-title feat-title">Featured services</h2>
  <p class="abs feat-text">There are many variations of passages of Lorem Ipsum available, but the majority have suffered alteration in some form, by injected humour, or randomised words which don't look even slightly believable. If you are going to use a passage of Lorem Ipsum, you need to be sure there isn't anything embarrassing hidden in the middle of text.</p>

  <article class="abs card" style="left:210px;top:1040px">
    <div class="card-img img-a" role="img" aria-label="Courier loading boxes into a van"></div>
    <h3>SERVICE ONE</h3>
    <p>There are many variations of passages of Lorem Ipsum available, but the majority have suffered alteration in some form</p>
  </article>
  <article class="abs card" style="left:609px;top:1040px">
    <div class="card-img img-b" role="img" aria-label="White delivery van driving on a road"></div>
    <h3>SERVICE TWO</h3>
    <p>There are many variations of passages of Lorem Ipsum available, but the majority have suffered alteration in some form</p>
  </article>
  <article class="abs card" style="left:210px;top:1175px">
    <div class="card-img img-c" role="img" aria-label="Worker packing cardboard boxes in a warehouse"></div>
    <h3>SERVICE THREE</h3>
    <p>There are many variations of passages of Lorem Ipsum available, but the majority have suffered alteration in some form</p>
  </article>
  <article class="abs card" style="left:609px;top:1175px">
    <div class="card-img img-a" role="img" aria-label="Courier loading boxes into a van"></div>
    <h3>SERVICE ONE</h3>
    <p>There are many variations of passages of Lorem Ipsum available, but the majority have suffered alteration in some form</p>
  </article>
</section>

<section>
  <h2 class="abs section-title news-title">Latest news</h2>
  <a class="abs view-all">VIEW ALL</a>

  <div class="abs news-img" style="left:210px;top:1439px;background:linear-gradient(135deg,#e8eaee,#5d6d8c 60%,#2d3a5c)" role="img" aria-label="Delivery worker with a clipboard beside a van"></div>
  <div class="abs news-date" style="left:410px;top:1428px">21<small>/june</small></div>
  <div class="abs news-head" style="left:410px;top:1485px">LATEST NEWS TITLE</div>
  <p class="abs news-text" style="left:410px;top:1508px">There are many variations of passages of Lorem Ipsum available, but the majority have suffered alteration in some form but the majority</p>
  <a class="abs btn small-btn news-btn" style="left:410px;top:1592px">READ MORE
    <svg width="10" height="10" viewBox="0 0 12 12"><path d="M2 6h8M6 2l4 4-4 4" stroke="#fff" stroke-width="2" fill="none"/></svg></a>

  <div class="abs news-img" style="left:609px;top:1439px;background:linear-gradient(135deg,#d8c4a0,#b08a5a 55%,#6e5a44)" role="img" aria-label="Stack of cardboard parcels"></div>
  <div class="abs news-date" style="left:809px;top:1428px">19<small>/june</small></div>
  <div class="abs news-head" style="left:809px;top:1485px">LATEST NEWS TITLE</div>
  <p class="abs news-text" style="left:809px;top:1508px">There are many variations of passages of Lorem Ipsum available, but the majority have suffered alteration in some form but the majority</p>
  <a class="abs btn small-btn news-btn" style="left:809px;top:1592px">READ MORE
    <svg width="10" height="10" viewBox="0 0 12 12"><path d="M2 6h8M6 2l4 4-4 4" stroke="#fff" stroke-width="2" fill="none"/></svg></a>
</section>

<section>
  <h2 class="abs section-title clients-title">Our clients</h2>
  <div class="abs client" style="left:208px">Pellwin</div>
  <div class="abs client" style="left:410px">Cyclorra</div>
  <div class="abs client" style="left:620px"><i></i>Marvello's</div>
  <div class="abs client" style="left:822px">Stillpoint</div>
</section>

<section>
  <div class="abs map" role="img" aria-label="Road map of the southern United States with a location marker"></div>
  <svg class="abs map-pin" viewBox="0 0 40 58"><path d="M20 0C9 0 0 9 0 20c0 14 20 38 20 38s20-24 20-38C40 9 31 0 20 0z" fill="#1d1a5c"/><circle cx="20" cy="19" r="7" fill="#fff"/></svg>
  <div class="abs contact-box">
    <h2>CONTACT US</h2>
    <ul>
      <li><svg viewBox="0 0 24 24"><path d="M6 2l4 4-2 3c1.5 3 4 5.5 7 7l3-2 4 4-3 4C10 21 3 14 2 5z" fill="#fff"/></svg>555-210-4470</li>
      <li><svg viewBox="0 0 24 24"><rect x="3" y="9" width="18" height="11" fill="#fff"/><rect x="6" y="3" width="12" height="6" fill="none" stroke="#fff" stroke-width="2"/></svg>555-210-4470</li>
      <li><svg viewBox="0 0 24 24"><rect x="2" y="5" width="20" height="14" fill="#fff"/><path d="M2 5l10 8 10-8" stroke="#1d1a5c" stroke-width="2" fill="none"/></svg>hello@kwuzo.com</li>
      <li><svg viewBox="0 0 24 24"><path d="M12 1C7 1 4 5 4 9c0 6 8 14 8 14s8-8 8-14c0-4-3-8-8-8z" fill="#fff"/><circle cx="12" cy="9" r="3" fill="#1d1a5c"/></svg>Westhaven</li>
    </ul>
  </div>
</section>

<footer>
  <div class="abs footer"></div>
  <div class="abs fcol" style="left:212px"><h4>Company</h4><ul><li>Home</li><li>About Us</li><li>Services</li><li>News</li><li>Contact Us</li></ul></div>
  <div class="abs fcol" style="left:410px"><h4>Services</h4><ul><li>Services 1</li><li>Services 2</li><li>Services 3</li></ul></div>
  <div class="abs fcol" style="left:610px"><h4>Locations</h4>
    <ul class="loc"><li>Ashbrook</li><li>Corrin</li><li>Delvale</li><li>Elmsford</li><li>Harlow Creek</li><li>Kestrel</li><li>Millbank</li><li>Norwood</li><li>Oakhurst</li><li>Pinecrest</li><li>Quarry</li><li>Redfield</li><li>Stonebridge</li><li>Tarrowvale</li><li>Wexley</li></ul></div>
  <div class="abs fcol" style="left:809px"><h4>Contact Us</h4><p>Main Office: 555-210-4470</p><p>Fax: 555-210-4471</p></div>
  <div class="abs copyright">Copyright © Brisk Lark 2016. All rights reserved.</div>
</footer>

</body>
</html>
```